写真挿入は無し、メニュー、営業時間も別看板がありますので記載不要です。添付のロゴとイラストを挿入してください。看板は両面ですが1デザインでも構いません。
⚪店名 雪見坂ことり亭
⚪定食 お酒 または、お食事 呑み処 など(デザインとのバランスでお願いします。)
⚪お気軽にどうぞ、気軽に来店ください など(安心して気軽に入店しやすくなる1フレーズ)
⚪イラストにふき出しで発声させてください。(フレーズはお任せします。)
⚪サイズは450mm×1300mmで縦長です。納品はaiデータです。
⚪文字色、全体的なデザインはお任せですが、背景色は薄ピンクが希望色です。グラデーションも好きです。イラスト、ロゴとのバランスでお願いします。
私ai使えませんので確認は別形式でお願いします。

見やすくバランスが良く丁度良いです。

また、よろしくお願いいたします。

```html
<!DOCTYPE html>
<html lang="ja">
<head>
<meta charset="UTF-8">
<title>雪見坂ことり亭 電飾看板</title>
<link href="https://fonts.googleapis.com/css2?family=Yuji+Mai&family=M+PLUS+Rounded+1c:wght@500;800&display=swap" rel="stylesheet">
<style>
  :root {
    --sheet: #ffffff;
    --label: #333333;
    --pink-deep: #e4588a;
    --pink-mid: #f4a9c0;
    --pink-soft: #fbd9e3;
    --pink-pale: #fff0f4;
    --name: #8e5a2a;
    --roman: #d9467a;
    --badge: #e54a80;
    --badge-text: #ffffff;
    --bubble: #ffffff;
    --bubble-line: #e4588a;
    --bubble-text: #c23668;
    --figure-a: #f6b9cc;
    --figure-b: #b9d7a6;
    --seal: #d9534f;
  }
  * { margin: 0; padding: 0; box-sizing: border-box; }
  html, body { width: 846px; height: 1200px; overflow: hidden; background: var(--sheet); }
  .sheet { position: relative; width: 846px; height: 1200px; }
  .spec-label {
    position: absolute; top: 98px;
    font-family: "M PLUS Rounded 1c", sans-serif; font-weight: 500;
    font-size: 13px; color: var(--label);
  }
  .signboard {
    position: absolute; top: 135px; width: 344px; height: 1000px;
    border: 3px solid var(--pink-deep);
    background:
      radial-gradient(ellipse at 50% 35%, var(--pink-pale) 0%, rgba(255,240,244,0) 60%),
      linear-gradient(180deg, var(--pink-mid) 0%, var(--pink-soft) 30%, var(--pink-soft) 70%, var(--pink-mid) 100%);
    overflow: hidden;
  }
  .signboard--a { left: 51px; }
  .signboard--b { left: 451px; }
  .spec-label--a { left: 51px; }
  .spec-label--b { left: 451px; }

  .menu-badge {
    position: absolute; left: 22px; top: 40px; width: 96px; height: 96px;
    border-radius: 50%; background: var(--badge);
    display: flex; flex-direction: column; align-items: center; justify-content: center;
    font-family: "M PLUS Rounded 1c", sans-serif; font-weight: 800;
    color: var(--badge-text); font-size: 19px; line-height: 1.25;
  }
  .shop-name {
    position: absolute; right: 18px; top: 60px; height: 460px;
    writing-mode: vertical-rl;
    font-family: "Yuji Mai", serif; font-size: 104px; line-height: 1.05;
    color: var(--name);
  }
  .shop-roman {
    position: absolute; right: 20px; top: 540px;
    font-family: "M PLUS Rounded 1c", sans-serif; font-weight: 800;
    font-size: 15px; color: var(--roman); letter-spacing: 0.5px;
  }
  .seal {
    position: absolute; left: 26px; top: 470px; width: 22px; height: 26px;
    border: 2px solid var(--seal); border-radius: 3px;
  }
  .character {
    position: absolute; left: 40px; top: 570px; width: 210px; height: 410px;
    border-radius: 100px 100px 20px 20px;
    background: linear-gradient(180deg, var(--figure-a) 0%, var(--figure-a) 55%, var(--figure-b) 75%, #ffffff 100%);
    opacity: 0.85;
  }
  .speech-bubble {
    position: absolute; right: 16px; top: 600px; width: 96px; height: 230px;
  }
  .speech-bubble svg { position: absolute; inset: 0; }
  .speech-text {
    position: absolute; inset: 16px 0 30px 0;
    display: flex; justify-content: center;
    writing-mode: vertical-rl;
    font-family: "M PLUS Rounded 1c", sans-serif; font-weight: 800;
    font-size: 17px; line-height: 1.5; color: var(--bubble-text);
  }
</style>
</head>
<body>
<main class="sheet">
  <p class="spec-label spec-label--a">■電飾看板（450×1,300）</p>
  <p class="spec-label spec-label--b">■電飾看板（450×1,300）</p>

  <section class="signboard signboard--a">
    <div class="menu-badge"><span>お食事</span><span>呑み処</span></div>
    <h1 class="shop-name">雪見坂<br>ことり亭</h1>
    <p class="shop-roman">yukimizaka kotoritei</p>
    <div class="seal"></div>
    <div class="character" role="img" aria-label="着物と袴姿の看板娘のイラスト（正面、会釈）"></div>
    <div class="speech-bubble">
      <svg viewBox="0 0 96 230" width="96" height="230">
        <path d="M48 4 C80 4 92 20 92 48 L92 170 C92 196 80 206 48 206 L30 206 L8 226 L16 202 C8 196 4 186 4 170 L4 48 C4 20 16 4 48 4 Z"
              fill="var(--bubble)" stroke="var(--bubble-line)" stroke-width="3"/>
      </svg>
      <p class="speech-text">どうぞお気軽に<br>ご来店くださいませ</p>
    </div>
  </section>

  <section class="signboard signboard--b">
    <div class="menu-badge"><span>お食事</span><span>呑み処</span></div>
    <h2 class="shop-name">雪見坂<br>ことり亭</h2>
    <p class="shop-roman">yukimizaka kotoritei</p>
    <div class="seal"></div>
    <div class="character" role="img" aria-label="着物と袴姿の看板娘のイラスト（正面、笑顔）"></div>
    <div class="speech-bubble">
      <svg viewBox="0 0 96 230" width="96" height="230">
        <path d="M48 4 C80 4 92 20 92 48 L92 170 C92 196 80 206 48 206 L30 206 L8 226 L16 202 C8 196 4 186 4 170 L4 48 C4 20 16 4 48 4 Z"
              fill="var(--bubble)" stroke="var(--bubble-line)" stroke-width="3"/>
      </svg>
      <p class="speech-text">どうぞお気軽に<br>ご来店くださいませ</p>
    </div>
  </section>
</main>
</body>
</html>
```